Rooted and RISING - community, webpage for workshop

I'm a pastoral counselor and teach workshops on non-violent communication and recovery from painful experiences. I have a website tamblewood.ca. I want a webpage designed for my workshops that will be integrated into my current website, then I can email the link, put it on fb or twitter. It will have a button for registration and payment using PayPal(already set up).

I'd like to look to be the same as on my website, using similiar colours. Note: My business card uses my photo (on the website) as its main design.

Size: to show on a single page when opened with little scrolling.

Target Market(s)

individuals and couples who have gone through difficult losses- divorce, death, loss of jobs & dreams & will be sent to professionals for referrals.

Industry/Entity Type

Communication

Requirements
Must have
• Will include online registration. Must include all the information needed. Warm inviting yet professional feel.
Nice to have
• Our photos
Should not have
• bright primary colours, cartoon graphics like butterflys, or be visually cluttered.

```html
<!DOCTYPE html>
<html lang="en">
<head>
<meta charset="utf-8">
<title>Tamblewood – Rooted and RISING Workshop</title>
<link href="https://fonts.googleapis.com/css2?family=Rosario:wght@300;400;600&family=Ubuntu+Condensed&family=Cabin:wght@400;600&display=swap" rel="stylesheet">
<style>
:root{
  --wood-dark:#3a1a0c;
  --wood-mid:#6b3518;
  --wood-light:#8a4a24;
  --cocoa:#2d150b;
  --panel:#ffffff;
  --panel-grey:#f1efec;
  --text:#2a1a10;
  --heading:#3d1f10;
  --logo:#f1c9a3;
  --nav-text:#f6e6d6;
}
*{margin:0;padding:0;box-sizing:border-box}
html,body{width:935px;height:1200px;overflow:hidden}
body{
  position:relative;
  font-family:"Cabin",sans-serif;
  color:var(--text);
  background:
    repeating-linear-gradient(90deg,rgba(0,0,0,.06) 0 3px,transparent 3px 22px,rgba(255,255,255,.03) 22px 25px,transparent 25px 41px),
    linear-gradient(90deg,var(--wood-dark) 0%,var(--wood-mid) 12%,var(--wood-light) 50%,var(--wood-mid) 88%,var(--wood-dark) 100%);
}
.logo{position:absolute;left:86px;top:36px;font-family:"Rosario",sans-serif;font-size:30px;color:var(--logo);font-weight:400}
.search{position:absolute;left:672px;top:61px;width:176px;height:24px;background:#fff;border-radius:12px;font-size:11px;padding:5px 12px;color:#333}
.search svg{position:absolute;right:9px;top:5px}
.nav{position:absolute;left:74px;top:97px;width:787px;height:43px;background:linear-gradient(#5a2a12,#3e1c0c);border-radius:6px 6px 0 0;display:flex;font-family:"Ubuntu Condensed",sans-serif;font-size:12px;color:var(--nav-text)}
.nav span{display:flex;align-items:center;justify-content:center;border-right:1px solid rgba(0,0,0,.35);padding:0 18px}
.nav span:last-child{border-right:none;flex:1}
.page{position:absolute;left:74px;top:140px;width:787px;height:1023px;background:var(--panel);border-radius:10px 10px 40px 40px/10px 10px 14px 14px}
.hero{position:absolute;left:11px;top:13px;width:755px;height:305px;background:var(--panel-grey);box-shadow:0 6px 8px -4px rgba(0,0,0,.25)}
.hero h1{position:absolute;left:37px;top:42px;font-family:"Rosario",sans-serif;font-weight:300;font-size:24px;line-height:31px;color:var(--heading)}
.hero .lead{position:absolute;left:37px;top:112px;width:270px;font-size:10.5px;font-weight:600;line-height:15px;color:var(--heading)}
.hero .body{position:absolute;left:37px;top:148px;width:290px;font-size:8.5px;line-height:15.5px;color:var(--heading)}
.btn{display:inline-block;background:var(--cocoa);color:#f5e6d8;font-family:"Ubuntu Condensed",sans-serif;border-radius:3px}
.hero .btn{position:absolute;left:35px;top:226px;width:70px;height:26px;font-size:12px;line-height:26px;text-align:center}
.video{position:absolute;left:367px;top:26px;width:365px;height:249px;background:var(--cocoa);border:3px solid #3e1f10;display:flex;align-items:center;justify-content:center}
.photo{position:absolute;border:3px solid #fff;box-shadow:0 0 3px rgba(0,0,0,.3);background:linear-gradient(#d8d4ce,#a89684)}
.card{position:absolute;font-size:9px;line-height:15.5px}
.card h2{font-family:"Rosario",sans-serif;font-weight:400;font-size:14.5px;line-height:18px;color:var(--cocoa);margin-bottom:6px}
.card strong{display:block;font-weight:600;margin-top:4px}
.small-btn{font-size:8.5px;padding:4px 8px;margin-top:6px}
.divider{position:absolute;left:16px;top:535px;width:746px;border-top:1px dotted #777}
.section h2{font-family:"Rosario",sans-serif;font-weight:400;font-size:16px;color:var(--cocoa)}
.about{position:absolute;left:20px;top:565px;width:480px;font-size:8.5px;line-height:17px}
.about p{margin-top:6px}
.about p.first{font-size:9px}
.about p.rest{font-size:7.8px}
.register{position:absolute;left:520px;top:565px;width:240px;font-size:9px;line-height:15px}
.register .btn{font-size:11px;padding:3px 9px;margin:10px 0 5px 2px}
.register p{padding-left:2px}
.info{position:absolute;left:19px;top:726px;width:747px;height:187px;background:linear-gradient(#f0eeec,#fafafa 50%,#efedea)}
.info .col{position:absolute;top:23px;font-size:8.8px;line-height:15.5px}
.info h2{font-family:"Rosario",sans-serif;font-weight:400;font-size:15.5px;line-height:23px;color:var(--cocoa);margin-bottom:6px}
.info p{margin-bottom:4px}
.footer{position:absolute;left:19px;top:945px;width:749px;border-top:1px solid #ddd;padding-top:14px;font-size:7.5px;font-weight:600;display:flex;justify-content:space-between}
.footer nav span{margin-left:22px}
</style>
</head>
<body>
<div class="logo">Tamblewood</div>
<div class="search">search..
  <svg width="13" height="13" viewBox="0 0 13 13"><circle cx="5.5" cy="5.5" r="4" fill="none" stroke="#222" stroke-width="2"/><line x1="8.5" y1="8.5" x2="12" y2="12" stroke="#222" stroke-width="2.2"/></svg>
</div>
<div class="nav">
  <span style="padding:0 26px">HOME</span><span>ROOTED AND RISING</span><span>COUNSELLING</span><span>ABOUT OWEN &amp; CLARE</span><span>LET’S TALK COMMUNICATION WORKSHOPS</span><span>CONTACT US</span>
</div>
<main class="page">
  <section class="hero">
    <h1>Everyone needs HOPE<br>But few know how to find it...</h1>
    <p class="lead">Curabitur tristique mi condimentum orci. Phasellus pellentesque aliquam enim.</p>
    <p class="body">Proin dui lectus, cursus eu, mattis laoreet, viverra sit amet, quam. Curabitur vel dolor ultrices ipsum dictum tristique. Praesent vitae lacus. Ut velit enim, vestibulum non, fermentum nec, hendrerit quis, leo. Pellentesque rutrum malesuada neque.</p>
    <span class="btn">MORE</span>
    <div class="video" role="img" aria-label="Workshop introduction video">
      <svg width="56" height="56" viewBox="0 0 56 56"><circle cx="28" cy="28" r="25.5" fill="none" stroke="#fff" stroke-width="3"/><polygon points="22,17 22,39 39,28" fill="#fff"/></svg>
    </div>
  </section>
  <div class="photo" role="img" aria-label="Portrait photo of Owen" style="left:19px;top:350px;width:127px;height:155px"></div>
  <div class="card" style="left:160px;top:350px;width:200px">
    <h2>What is ‘Rooted and RISING for the Community’?</h2>
    Rooted and RISING for the Community is a 2-day workshop that will teach you a process will enable you to find and keep HOPE:
    <strong style="margin-top:8px">Resolve emotional loss</strong>
    <strong>End isolation and self-sabotage</strong>
    <span class="btn small-btn">READ MORE</span>
  </div>
  <div class="photo" role="img" aria-label="Portrait photo of Clare" style="left:397px;top:347px;width:127px;height:158px"></div>
  <div class="card" style="left:539px;top:347px;width:210px">
    <h2 style="margin-bottom:4px">Who is it for?</h2>
    <p style="font-size:10px;margin-bottom:5px;padding-left:2px">Adults and Youth age 18 +.</p>
    <p style="padding-left:2px">Whether this is your first attempt to heal from a difficult experience, or just another step on a longer journey, this workshop has been designed to facilitate healing and HOPE at whatever point you are at.</p>
    <span class="btn small-btn" style="margin-left:2px">READ MORE</span>
  </div>
  <div class="divider"></div>
  <section class="about section">
    <h2>About the Facilitators:</h2>
    <p class="first">Owen and Clare Marsden draw on more than 30 years of marriage, parenting and ministry experience to help spouses, parents and individuals continue to learn and grow personally and in their most important relationships.</p>
    <p class="rest">They have conducted numerous workshops and retreats and have been keynote speakers at events both large and small all throughout Canada, the U.S., and in Turkey, Israel, Cyprus and Greece. Owen is a certified coach and trainer using the Growing Through Strengths model (www.strengthsguidepro.com) and also offers training in Nonviolent Communication. Clare is a Registered Professional Counsellor, is licensed to provide HOPE Workshops (www.hopecircleresources.com)</p>
  </section>
  <section class="register section">
    <h2>How do I register for the Workshop?</h2>
    <span class="btn">CLICK HERE</span>
    <p>or copy and paste into your browser:</p>
    <p>http://tamblewood.ca/about-rooted-and-rising/rr-registr<br>ation-payment/</p>
  </section>
  <section class="info">
    <div class="col" style="left:26px;width:230px">
      <h2>When is it?</h2>
      <p style="padding-left:2px">Friday November 2nd from 6:30pm to 9:30pm AND Saturday November 3rd from 9:00am to 5:00pm</p>
      <p style="padding-left:2px">Riverside Hall 604.555.0142</p>
      <p style="padding-left:2px">2240 Cedar Lane, Vancouver, BC V5K 0A1</p>
    </div>
    <div class="col" style="left:273px;width:215px">
      <h2>Will I have to share in<br>front of others?</h2>
      <p style="text-align:justify">No. Though you will learn in a safe group environment, ‘Rooted and RISING for the Community’ is an individual process. You’ll choose one listening partner to keep all weekend.</p>
    </div>
    <div class="col" style="left:534px;width:200px">
      <h2>What are the fees and<br>important details?</h2>
      <p style="padding-left:2px;font-weight:600;font-size:10px">Fees:</p>
      <p style="padding-left:2px">Early Bird registration before October 15th - $205 &nbsp;|&nbsp; After October 15th - $225</p>
      <p style="padding-left:2px">Registration Includes Workshop and Snacks.</p>
      <p style="padding-left:2px">Please note we will have a working lunch.</p>
    </div>
  </section>
  <footer class="footer">
    <span>© 2012 - Tamblewood is powered by Pressbench</span>
    <nav><span>Home</span><span>Rooted and RISING</span><span>Counselling</span><span>About Owen &amp; Clare</span><span>Let’s Talk Communication Workshops</span><span>Contact us</span></nav>
  </footer>
</main>
</body>
</html>
```